Natural Product Labels

We need product Labels for our natural product company called Teluko. We currently have a logo that I have attached. I would like the label to have an African theme. Use of brown, green and purple is preferred. Designs can include tree bark and/or leaves but is not required. The products are natural body butters and lotions scented with fruit flavors.
Label Sizes: Length x Height
Jar - 0.9375" x 9.0625"
Bottle – 7“ x 3”
We have 5 product types that we will need to be change the label to suit without too much modification.
Sample Label Information is as follows
Natural Cocoa Butter
tone moisturize soften
OAT EXTRACT and ALMOND OIL
Normal to Dry skin
Net Weight: 4oz
Beauty Secrets from the African Tropics
Ingredients: Oat Infusion(Water and Oats), Cocoa butter, Almond oil, Glycerin, Shea butter, Glyceryl Stearate, Cetearyl Alchohol, Sodium Stearoyl Lactylate, Cocoa powder, Fragrance, Phenoxyethanol, Caprylyl Glycol, Xanthan Gum
Teluko Naturals LLC
www.telukonaturals.example
Reason: I need more designs to compare. I have had some designers accept the project but have not sent any designs yet.

```html
<!DOCTYPE html>
<html lang="en">
<head>
<meta charset="utf-8">
<title>Teluko – Natural Body Butter Labels</title>
<link href="https://fonts.googleapis.com/css2?family=Delius&family=Josefin+Sans:wght@300;400&family=Open+Sans:wght@400&display=swap" rel="stylesheet">
<style>
  :root {
    --bark: #4a2a17;
    --bark-mid: #6b4426;
    --taupe: #a89684;
    --leaf: #a6c83a;
    --leaf-dark: #8db32a;
    --plum: #7a4da3;
    --plum-deep: #6e1f6b;
    --cream: #fbf1e3;
    --cream-warm: #f7e3c8;
    --peach: #f6d9b4;
    --halo: #ece7df;
    --ink: #5a3a22;
    --melon: #e1a43d;
    --melon-rind: #9a8a2c;
    --peach-fruit: #d9602a;
    --pear: #d8dc3c;
    --apple: #e0422e;
    --berry: #d93a3a;
    --skin: #e8c9a8;
  }
  html, body { margin: 0; padding: 0; }
  body {
    width: 1200px; height: 1065px; overflow: hidden;
    background: #ffffff;
  }
  .label-sheet { display: block; width: 1200px; height: 1065px; }
  .tagline { font-family: "Josefin Sans", sans-serif; font-weight: 300; fill: var(--leaf); letter-spacing: 2px; }
  .brand-name { font-family: "Josefin Sans", sans-serif; font-weight: 400; fill: var(--plum); }
  .product-type { font-family: "Delius", cursive; fill: var(--ink); }
  .detail-text { font-family: "Open Sans", sans-serif; fill: var(--ink); }
</style>
</head>
<body>
<svg class="label-sheet" viewBox="0 0 1200 1065" xmlns="http://www.w3.org/2000/svg">
  <defs>
    <radialGradient id="cream-glow" cx="50%" cy="45%" r="60%">
      <stop offset="0" stop-color="#ffffff"/>
      <stop offset="1" stop-color="var(--cream-warm)"/>
    </radialGradient>
    <radialGradient id="pearl-glow" cx="50%" cy="50%" r="60%">
      <stop offset="0" stop-color="#ffffff"/>
      <stop offset="1" stop-color="#efe6da"/>
    </radialGradient>
    <linearGradient id="portrait-tones" x1="0" y1="0" x2="0" y2="1">
      <stop offset="0" stop-color="#d9c08a" stop-opacity="0.55"/>
      <stop offset="1" stop-color="#e9b9a8" stop-opacity="0.35"/>
    </linearGradient>
    <path id="oval-arc" d="M110,200 A240,150 0 0 1 545,200"/>
    <path id="frame-arc" d="M805,130 Q960,70 1115,130"/>
    <path id="ornate-frame" d="M179,4 C250,4 300,30 315,85 C332,95 347,112 347,137 C347,165 356,185 356,218 C356,262 346,300 331,330 C318,362 298,386 268,396 C238,406 213,420 179,422 C145,420 120,406 90,396 C60,386 40,362 27,330 C12,300 2,262 2,218 C2,185 11,165 11,137 C11,112 26,95 43,85 C58,30 108,4 179,4 Z"/>
  </defs>

  <!-- Oval jar label -->
  <g class="label label--oval">
    <ellipse cx="325" cy="240" rx="324" ry="236" fill="var(--bark)"/>
    <ellipse cx="325" cy="240" rx="298" ry="212" fill="var(--taupe)"/>
    <ellipse cx="325" cy="240" rx="291" ry="205" fill="var(--leaf)"/>
    <ellipse cx="325" cy="240" rx="280" ry="194" fill="var(--cream)"/>
    <text class="tagline" font-size="40">
      <textPath href="#oval-arc" startOffset="4%">NATURE</textPath>
    </text>
    <text class="tagline" font-size="40">
      <textPath href="#oval-arc" startOffset="50%">INSPIRED</textPath>
    </text>
    <text class="brand-name" x="290" y="248" font-size="86" text-anchor="middle">Teluko</text>
    <text class="product-type" x="310" y="290" font-size="19" text-anchor="middle">natural body butter</text>
    <g class="detail-block">
      <ellipse cx="453" cy="192" rx="56" ry="29" fill="none" stroke="var(--bark-mid)" stroke-width="1"/>
      <text class="detail-text" x="453" y="180" font-size="6.5" text-anchor="middle">SAMPLE TEXT</text>
      <text class="detail-text" x="453" y="192" font-size="6.5" text-anchor="middle">SAMPLE TEXT  SAMPLE TEXT</text>
      <text class="detail-text" x="453" y="201" font-size="6.5" text-anchor="middle">SAMPLE TEXT  SAMPLE TEXT</text>
      <text class="detail-text" x="453" y="210" font-size="6.5" text-anchor="middle">SAMPLE TEXT  SAMPLE TEXT</text>
    </g>
    <g class="fruit-set">
      <ellipse cx="82" cy="220" rx="26" ry="20" fill="var(--peach-fruit)" role="img" aria-label="Illustrated peaches"/>
      <ellipse cx="556" cy="232" rx="26" ry="20" fill="var(--peach-fruit)" role="img" aria-label="Illustrated peaches"/>
      <ellipse cx="117" cy="308" rx="20" ry="27" fill="var(--pear)" role="img" aria-label="Illustrated pear"/>
      <ellipse cx="529" cy="312" rx="20" ry="27" fill="var(--pear)" role="img" aria-label="Illustrated pear"/>
      <ellipse cx="199" cy="358" rx="38" ry="25" fill="var(--melon)" role="img" aria-label="Illustrated cut melon"/>
      <ellipse cx="445" cy="358" rx="38" ry="25" fill="var(--melon)" role="img" aria-label="Illustrated cut melon"/>
      <circle cx="291" cy="384" r="20" fill="var(--apple)" role="img" aria-label="Illustrated apple"/>
      <ellipse cx="359" cy="384" rx="19" ry="23" fill="var(--berry)" role="img" aria-label="Illustrated strawberry"/>
    </g>
  </g>

  <!-- Framed bottle label -->
  <g class="label label--framed">
    <path d="M767,27 H1151 A30,30 0 0 0 1181,57 V412 A30,30 0 0 0 1151,442 H767 A30,30 0 0 0 737,412 V57 A30,30 0 0 0 767,27 Z" fill="var(--peach)"/>
    <path d="M778,42 H1140 A24,24 0 0 0 1164,66 V403 A24,24 0 0 0 1140,427 H778 A24,24 0 0 0 754,403 V66 A24,24 0 0 0 778,42 Z" fill="url(#cream-glow)" stroke="var(--bark-mid)" stroke-width="3"/>
    <path d="M784,52 H1134 A20,20 0 0 0 1154,72 V397 A20,20 0 0 0 1134,417 H784 A20,20 0 0 0 764,397 V72 A20,20 0 0 0 784,52 Z" fill="none" stroke="var(--bark-mid)" stroke-width="1.5"/>
    <text class="tagline" font-size="29">
      <textPath href="#frame-arc" startOffset="0%">NATURE</textPath>
    </text>
    <text class="tagline" font-size="29">
      <textPath href="#frame-arc" startOffset="52%">INSPIRED</textPath>
    </text>
    <ellipse cx="953" cy="80" rx="17" ry="11" fill="var(--melon)" role="img" aria-label="Small illustrated melon"/>
    <text class="brand-name" x="952" y="272" font-size="80" text-anchor="middle">Teluko</text>
    <path d="M1070,296 C1072,268 1092,254 1118,252 C1116,278 1098,296 1070,296 Z" fill="var(--leaf-dark)" role="img" aria-label="Green leaf"/>
    <text class="product-type" x="958" y="312" font-size="20" text-anchor="middle">natural body butter</text>
    <g class="detail-block">
      <ellipse cx="961" cy="373" rx="69" ry="27" fill="none" stroke="var(--bark-mid)" stroke-width="1"/>
      <text class="detail-text" x="961" y="356" font-size="7" text-anchor="middle">SAMPLE TEXT</text>
      <text class="detail-text" x="961" y="370" font-size="7" text-anchor="middle">SAMPLE TEXT   SAMPLE TEXT</text>
      <text class="detail-text" x="961" y="379" font-size="7" text-anchor="middle">SAMPLE TEXT   SAMPLE TEXT</text>
      <text class="detail-text" x="961" y="388" font-size="7" text-anchor="middle">SAMPLE TEXT   SAMPLE TEXT</text>
    </g>
  </g>

  <!-- Ornate bottle label -->
  <g class="label label--ornate">
    <g transform="translate(401,478) scale(1.373)">
      <use href="#ornate-frame" fill="var(--halo)"/>
      <use href="#ornate-frame" transform="translate(179,213) scale(0.9) translate(-179,-213)" fill="url(#pearl-glow)" stroke="var(--bark-mid)" stroke-width="3"/>
      <use href="#ornate-frame" transform="translate(179,213) scale(0.875) translate(-179,-213)" fill="none" stroke="var(--plum-deep)" stroke-width="3.5"/>
      <use href="#ornate-frame" transform="translate(179,213) scale(0.85) translate(-179,-213)" fill="none" stroke="var(--bark-mid)" stroke-width="2.5"/>
    </g>
    <path d="M545,590 C545,520 600,500 650,505 C705,510 730,545 728,600 L740,760 L545,760 Z" fill="url(#portrait-tones)" role="img" aria-label="Faded illustration of a woman with long hair"/>
    <text class="product-type" x="652" y="641" font-size="19" text-anchor="middle">natural body butter</text>
    <text class="brand-name" x="645" y="790" font-size="80" text-anchor="middle">Teluko</text>
    <text class="tagline" x="652" y="822" font-size="27" text-anchor="middle">NATURE INSPIRED</text>
    <g class="detail-block">
      <text class="detail-text" x="652" y="868" font-size="11" text-anchor="middle">SAMPLE TEXT   SAMPLE TEXT   SAMPLE TEXT</text>
      <text class="detail-text" x="652" y="885" font-size="11" text-anchor="middle">SAMPLE TEXT   SAMPLE TEXT</text>
      <text class="detail-text" x="652" y="902" font-size="11" text-anchor="middle">SAMPLE TEXT</text>
    </g>
    <ellipse cx="645" cy="950" rx="46" ry="28" fill="var(--melon)" role="img" aria-label="Illustrated cut melon"/>
  </g>
</svg>
</body>
</html>
```